Business Card Re-Design/Update

We'd like to update out business cards. I've included our current "Style guide" which has the colour scheme of the organisation in it. I've also included the branding files with logos etc in them.

I've also included a copy of one of our existing cards so that you can see how ugly/dated they look. I'd like a fresh modern corporate look.

Target Market(s)

These are for our clients, potential clients, industry contacts - like all business cards

Contact Information for Business Card

Name
Position
Company Address - Level 1, 47 Garnet Lane, Toowong Qld 4066
Direct Phone
mobile
Email
Website -www.korvalnet.com.au
Logo

Colors

Designer to choose colors to be used in the design.

Requirements
Must have
• Main Logo
• Cards will need to be editable to be able to personalize them for each new employee.
Nice to have
• The MapOUT, HandOVER, UpKEEP would be okay to have if they can be sensibly and professionally added to the look without detracting from the main imagery.
• Maybe they could go on the back of the card? will leave this to your creative discretion as to whether/where they fit.
Should not have
• Should not have decorative or script fonts

```html
<!DOCTYPE html>
<html lang="en">
<head>
<meta charset="utf-8">
<title>korvalnet business card</title>
<link rel="stylesheet" href="https://fonts.googleapis.com/css2?family=Arimo:wght@400;700&display=swap">
<style>
  :root {
    --stage: #ababab;
    --card-top: #3b3b3d;
    --card-bottom: #262628;
    --red: #d8363b;
    --white: #ffffff;
    --blue: #3b8fd9;
    --green: #6fb544;
    --magenta: #c23fa6;
  }
  * { margin: 0; padding: 0; box-sizing: border-box; }
  html, body { width: 900px; height: 1200px; overflow: hidden; }
  body {
    position: relative;
    background: var(--stage);
    font-family: "Arimo", Arial, sans-serif;
    color: var(--white);
  }
  .card {
    position: absolute;
    left: 143px;
    width: 613px;
    height: 389px;
    overflow: hidden;
  }
  .card--front { top: 82px; }
  .card--back { top: 633px; }
  .card__surface {
    position: absolute; inset: 0;
    background: linear-gradient(160deg, var(--card-top) 0%, #323234 50%, var(--card-bottom) 100%);
  }
  .edge-bar { position: absolute; width: 14px; }
  .edge-bar--left { left: 0; }
  .edge-bar--right { right: 0; }

  .brand {
    position: absolute;
    display: flex; align-items: center; gap: 12px;
    font-weight: 400;
    color: var(--white);
    letter-spacing: -0.5px;
  }
  .brand__mark { background: var(--red); flex: none; }
  .card--front .brand { left: 140px; top: 166px; font-size: 50px; }
  .card--front .brand__mark { width: 40px; height: 40px; }
  .card--back .brand { left: 50px; top: 174px; font-size: 32px; }
  .card--back .brand__mark { width: 26px; height: 26px; }

  .front-web {
    position: absolute; left: 210px; top: 238px;
    display: flex; align-items: center; gap: 15px;
    font-size: 15px;
  }

  .person { position: absolute; left: 315px; top: 40px; }
  .person__name { font-size: 24px; font-weight: 700; color: var(--red); letter-spacing: 0.2px; }
  .person__role { font-size: 17px; margin-top: 4px; }

  .phone-band {
    position: absolute; left: 306px; width: 307px; height: 49px;
    background: var(--red);
    padding: 4px 0 0 8px;
  }
  .phone-band--direct { top: 103px; }
  .phone-band--office { top: 157px; }
  .phone-line { display: flex; align-items: center; height: 20px; font-size: 15px; }
  .phone-line svg { width: 16px; height: 16px; margin-right: 14px; flex: none; }

  .detail { position: absolute; left: 314px; display: flex; font-size: 15px; line-height: 19px; }
  .detail__icon {
    width: 18px; height: 18px; background: var(--red); flex: none;
    margin-right: 12px; display: flex; align-items: center; justify-content: center;
  }
  .detail--address { top: 224px; }
  .detail--email { top: 270px; }
  .detail--web { top: 297px; }

  .services {
    position: absolute; right: 16px; top: 346px;
    display: flex; gap: 14px; font-size: 16px; font-weight: 700;
  }
  .service { display: flex; align-items: center; gap: 5px; }
  .service__mark { width: 11px; height: 11px; flex: none; }
  .service--handover { color: var(--blue); }
  .service--handover .service__mark { background: var(--blue); }
  .service--mapout { color: var(--green); }
  .service--mapout .service__mark { background: var(--green); }
  .service--upkeep { color: var(--magenta); }
  .service--upkeep .service__mark { background: var(--magenta); }
</style>
</head>
<body>

<section class="card card--front">
  <div class="card__surface" role="img" aria-label="Dark charcoal low-poly faceted background"></div>
  <svg class="edge-bar edge-bar--left" style="top:40px" width="14" height="308" viewBox="0 0 14 308">
    <polygon points="0,0 14,10 14,298 0,308" fill="var(--red)"/>
  </svg>
  <svg class="edge-bar edge-bar--right" style="top:40px" width="14" height="308" viewBox="0 0 14 308">
    <polygon points="14,0 0,10 0,298 14,308" fill="var(--red)"/>
  </svg>
  <div class="brand"><span class="brand__mark"></span>korvalnet</div>
  <div class="front-web">
    <svg width="17" height="17" viewBox="0 0 20 20" fill="none" stroke="var(--white)" stroke-width="1.6">
      <circle cx="10" cy="10" r="8.5"/><ellipse cx="10" cy="10" rx="3.8" ry="8.5"/>
      <line x1="1.5" y1="10" x2="18.5" y2="10"/><line x1="3" y1="5.5" x2="17" y2="5.5"/><line x1="3" y1="14.5" x2="17" y2="14.5"/>
    </svg>
    <span>www.korvalnet.com.au</span>
  </div>
</section>

<section class="card card--back">
  <div class="card__surface" role="img" aria-label="Dark charcoal low-poly faceted background"></div>
  <svg class="edge-bar edge-bar--left" style="top:42px" width="14" height="307" viewBox="0 0 14 307">
    <polygon points="0,0 14,10 14,297 0,307" fill="var(--red)"/>
  </svg>
  <div class="brand"><span class="brand__mark"></span>korvalnet</div>

  <div class="person">
    <div class="person__name">DANA WHITFIELD</div>
    <div class="person__role">Business Development Manager</div>
  </div>

  <div class="phone-band phone-band--direct">
    <div class="phone-line">
      <svg viewBox="0 0 16 16"><rect x="4" y="1" width="8" height="14" rx="1.5" fill="none" stroke="var(--white)" stroke-width="1.5"/><circle cx="8" cy="12.5" r="0.9" fill="var(--white)"/></svg>
      +61 (0)412 555 048
    </div>
    <div class="phone-line">
      <svg viewBox="0 0 16 16"><path d="M3 2l3 0 1 3-2 1.5a9 9 0 0 0 4.5 4.5L11 9l3 1 0 3c-6 1-12-5-11-11z" fill="var(--white)"/><path d="M10 1.5a5 5 0 0 1 4.5 4.5M10 4a2.5 2.5 0 0 1 2 2" fill="none" stroke="var(--white)" stroke-width="1.2"/></svg>
      +61 (0)7 3000 4172
    </div>
  </div>

  <div class="phone-band phone-band--office">
    <div class="phone-line">
      <svg viewBox="0 0 16 16"><path d="M1 6c0-3 14-3 14 0l0 1.5-3.5 0 0-1.5c-2-0.7-5-0.7-7 0l0 1.5L1 7.5z" fill="var(--white)"/><path d="M4 9h8l2 5H2z" fill="var(--white)"/></svg>
      +61 (0)7 3000 4100
    </div>
    <div class="phone-line">
      <svg viewBox="0 0 16 16"><rect x="4" y="1" width="8" height="5" fill="none" stroke="var(--white)" stroke-width="1.3"/><rect x="1" y="6" width="14" height="7" rx="1" fill="var(--white)"/><rect x="4" y="11" width="8" height="4" fill="var(--white)" stroke="var(--red)" stroke-width="0.8"/></svg>
      +61 (0)7 3000 4199
    </div>
  </div>

  <div class="detail detail--address">
    <span class="detail__icon"><svg width="10" height="12" viewBox="0 0 10 12"><path d="M5 0a4 4 0 0 0-4 4c0 3 4 8 4 8s4-5 4-8a4 4 0 0 0-4-4z" fill="var(--white)"/><circle cx="5" cy="4" r="1.5" fill="var(--red)"/></svg></span>
    <span>Level 1, 47 Garnet Lane, Toowong<br>Qld 4066</span>
  </div>
  <div class="detail detail--email">
    <span class="detail__icon"><svg width="11" height="8" viewBox="0 0 11 8"><rect x="0.5" y="0.5" width="10" height="7" fill="none" stroke="var(--white)"/><path d="M0.5 0.5l5 4 5-4" fill="none" stroke="var(--white)"/></svg></span>
    <span>whitfield@korvalnet.com.au</span>
  </div>
  <div class="detail detail--web">
    <span class="detail__icon"><svg width="11" height="11" viewBox="0 0 20 20" fill="none" stroke="var(--white)" stroke-width="2"><circle cx="10" cy="10" r="8.5"/><ellipse cx="10" cy="10" rx="3.8" ry="8.5"/><line x1="1.5" y1="10" x2="18.5" y2="10"/></svg></span>
    <span>www.korvalnet.com.au</span>
  </div>

  <div class="services">
    <span class="service service--handover"><span class="service__mark"></span>HandOVER</span>
    <span class="service service--mapout"><span class="service__mark"></span>MapOUT</span>
    <span class="service service--upkeep"><span class="service__mark"></span>UpKEEP</span>
  </div>
</section>

</body>
</html>
```